Resume build

I need someone to develop a resume for me. This needs to include a stylized template as well as improving the content of my existing resume.
Updates

All content generated. Just need resume to be formatted and stylized a few different options. With offer a few different head shots to go into it as well. Final versions to be in PDF.

Target Market(s)

this is not for finding a job but is for presenting to clients on who I am and why I'm the qualified candidate to perform their work.

Industry/Entity Type

Marine

Colors
0054AA
0677BA
7BADD7
CADEEF
E8F1F8

Requirements
Must have
• must be in PDF and have a location to add a picture later in the top corner

```html
<!DOCTYPE html>
<html lang="en">
<head>
<meta charset="utf-8">
<title>Rowan Kestell – Resume</title>
<link href="https://fonts.googleapis.com/css2?family=Montserrat:wght@500;600&family=Open+Sans:ital,wght@0,400;0,600;1,400&display=swap" rel="stylesheet">
<style>
  :root {
    --navy: #232b3e;
    --gold: #a8843f;
    --ink: #2b3245;
    --body: #555a63;
    --rule: #3a4256;
    --paper: #ffffff;
    --backdrop: #eeeff1;
    --photo: #8a8d91;
  }
  * { box-sizing: border-box; margin: 0; padding: 0; }
  html, body { width: 1200px; height: 840px; overflow: hidden; background: var(--backdrop); }
  .stage { position: relative; width: 1200px; height: 840px; }
  .page {
    position: absolute; left: 310px; top: 10px;
    width: 849px; height: 1202px;
    transform: scale(0.682); transform-origin: top left;
    background: var(--paper);
    font-family: "Open Sans", sans-serif; color: var(--body);
    box-shadow: 0 8px 30px rgba(0,0,0,.12);
  }
  .abs { position: absolute; }
  .header { left: 0; top: 0; width: 849px; height: 261px; background: var(--navy); }
  .name {
    left: 0; width: 849px; top: 68px; text-align: center;
    font-family: "Montserrat", sans-serif; font-weight: 600; font-size: 44px;
    letter-spacing: .14em; color: #fff;
  }
  .role-title {
    left: 0; width: 849px; top: 141px; text-align: center;
    font-family: "Montserrat", sans-serif; font-weight: 500; font-size: 14px;
    letter-spacing: .3em; color: var(--gold);
  }
  .gold-rule { height: 1px; background: var(--gold); top: 150px; width: 128px; }
  .contact { top: 194px; text-align: center; color: #fff; font-size: 11px; }
  .contact svg { display: block; margin: 0 auto 10px; }
  .contact-divider { top: 200px; width: 1px; height: 38px; background: #8a90a0; }
  .headshot { left: 57px; top: 277px; width: 182px; height: 182px; }
  .summary {
    left: 259px; top: 307px; width: 531px;
    font-size: 11.3px; line-height: 21.5px; text-align: justify;
  }
  .rule { height: 1.5px; background: var(--rule); }
  .vrule { left: 324px; top: 476px; width: 1.5px; height: 670px; background: var(--rule); }
  .section-title {
    font-family: "Montserrat", sans-serif; font-weight: 600; font-size: 16px;
    letter-spacing: .22em; color: var(--ink); text-align: center;
  }
  ul { list-style: none; }
  .skills { left: 63px; top: 557px; width: 226px; font-size: 12.5px; line-height: 20px; }
  .skills li, .duties li { position: relative; padding-left: 27px; text-align: justify; }
  .skills li { margin-bottom: 4px; }
  .skills li::before {
    content: ""; position: absolute; left: 3px; top: 8px;
    width: 5px; height: 5px; border-radius: 50%; background: var(--gold);
  }
  .edu { left: 61px; top: 931px; width: 250px; }
  .edu-item { margin-bottom: 18px; }
  .degree { font-weight: 600; font-size: 13.5px; color: var(--ink); line-height: 22px; }
  .school { font-style: italic; font-size: 12px; color: var(--gold); line-height: 22px; }
  .school .year { color: var(--body); }
  .work { left: 361px; top: 557px; width: 434px; }
  .work-intro { padding-left: 26px; font-size: 11.3px; line-height: 21.5px; text-align: justify; margin-bottom: 20px; }
  .employer {
    font-family: "Montserrat", sans-serif; font-weight: 500; font-size: 13.5px;
    letter-spacing: .08em; color: var(--ink); line-height: 24px;
  }
  .position { font-style: italic; font-size: 12.5px; color: var(--gold); line-height: 24px; margin-bottom: 4px; }
  .duties { padding-left: 26px; font-size: 11.3px; line-height: 21.5px; }
  .duties li { margin-bottom: 1px; }
  .duties li::before {
    content: ""; position: absolute; left: 3px; top: 9px;
    width: 4px; height: 4px; border-radius: 50%; background: var(--ink);
  }
  .duties.spaced li { line-height: 20px; margin-bottom: 8px; }
</style>
</head>
<body>
<div class="stage">
  <div class="page">
    <header class="abs header">
      <h1 class="abs name">ROWAN KESTELL</h1>
      <div class="abs gold-rule" style="left:58px"></div>
      <p class="abs role-title">MARINE PROJECT OPERATIONS MANAGER</p>
      <div class="abs gold-rule" style="left:665px"></div>

      <div class="abs contact" style="left:22px;width:220px">
        <svg width="22" height="16" viewBox="0 0 22 16"><rect width="22" height="16" fill="var(--gold)"/><path d="M0 0 L11 9 L22 0" stroke="var(--navy)" stroke-width="1.6" fill="none"/><path d="M0 16 L8 7 M22 16 L14 7" stroke="var(--navy)" stroke-width="1.2"/></svg>
        rowan@tidelinemarine.com
      </div>
      <div class="abs contact-divider" style="left:262px"></div>
      <div class="abs contact" style="left:290px;width:212px">
        <svg width="18" height="18" viewBox="0 0 24 24"><path fill="var(--gold)" d="M6.6 10.8a15.1 15.1 0 0 0 6.6 6.6l2.2-2.2c.3-.3.7-.4 1-.2 1.1.4 2.3.6 3.6.6.6 0 1 .4 1 1V20c0 .6-.4 1-1 1A17 17 0 0 1 3 4c0-.6.4-1 1-1h3.5c.6 0 1 .4 1 1 0 1.3.2 2.5.6 3.6.1.3 0 .7-.2 1z"/></svg>
        1 (555) 014 2290
      </div>
      <div class="abs contact-divider" style="left:537px"></div>
      <div class="abs contact" style="left:555px;width:285px">
        <svg width="22" height="16" viewBox="0 0 22 16"><rect width="22" height="16" fill="var(--gold)"/><path d="M0 0 L11 9 L22 0" stroke="var(--navy)" stroke-width="1.6" fill="none"/><path d="M0 16 L8 7 M22 16 L14 7" stroke="var(--navy)" stroke-width="1.2"/></svg>
        42 Harbourview Lane, Port Alder BC Canada, V0R 1K0
      </div>
    </header>

    <svg class="abs headshot" viewBox="0 0 182 182" role="img" aria-label="Headshot photo placeholder">
      <defs>
        <radialGradient id="photoTone" cx="50%" cy="40%" r="60%">
          <stop offset="0" stop-color="#b4b6b9"/>
          <stop offset="1" stop-color="var(--photo)"/>
        </radialGradient>
      </defs>
      <circle cx="91" cy="91" r="89" fill="url(#photoTone)" stroke="#1e2230" stroke-width="1.5"/>
    </svg>

    <p class="abs summary">As a Content Writer and Marketing Strategist with 11 years of industry experience, I possess a diverse skill set that includes writing for various platforms and managing campaigns across multiple channels. I am proficient in using PageForge, RankScope, SiteLoom, CourseNest, CartHaven, and MailSpring and can produce content for every phase of a sales funnel. With my commitment to transparency and meeting deadlines, you are guaranteed a professional service from start to finish. I have a proven track record of delivering successful marketing campaigns and I am always looking for new challenges to take on.</p>

    <div class="abs rule" style="left:63px;top:476px;width:250px"></div>
    <h2 class="abs section-title" style="left:63px;top:491px;width:250px">SKILLS</h2>
    <div class="abs rule" style="left:63px;top:525px;width:250px"></div>

    <div class="abs vrule"></div>

    <div class="abs rule" style="left:361px;top:476px;width:423px"></div>
    <h2 class="abs section-title" style="left:361px;top:492px;width:423px">WORK EXPERIENCE</h2>
    <div class="abs rule" style="left:361px;top:525px;width:423px"></div>

    <ul class="abs skills">
      <li>Excellent writing and communication skills</li>
      <li>Campaign creation and execution</li>
      <li>Creativity and innovation</li>
      <li>SEO Kills</li>
      <li>Social media marketing and content creation</li>
      <li>Complex project management.</li>
      <li>Research skills and versatility in writing topics</li>
      <li>Identifying marketing personas</li>
    </ul>

    <div class="abs rule" style="left:63px;top:866px;width:221px"></div>
    <h2 class="abs section-title" style="left:63px;top:880px;width:221px">EDUCATION</h2>
    <div class="abs rule" style="left:63px;top:913px;width:221px"></div>

    <div class="abs edu">
      <div class="edu-item">
        <p class="degree">Health Sciences BSc</p>
        <p class="school">WESTMERE UNIVERSITY <span class="year">- 2022</span></p>
      </div>
      <div class="edu-item">
        <p class="degree">Marketing Diploma</p>
        <p class="school">ALLIED INSTITUTE OF MARKETING -<br><span class="year">2019</span></p>
      </div>
      <div class="edu-item">
        <p class="degree">Psychotherapy Diploma</p>
        <p class="school">HALDEN COLLEGE <span class="year">- 2008</span></p>
      </div>
    </div>

    <div class="abs work">
      <p class="work-intro">As a freelance content and marketing manager, I've worked with numerous clients, ranging from individuals to large corporations. Recent clients include prominent organisations across various industries.</p>

      <h3 class="employer">The Northfield Institute of Ceremony Guides</h3>
      <p class="position">Marketing Manager/ 2021-2023</p>
      <ul class="duties">
        <li>Researched and wrote informative blog posts on wedding celebrant tips for LGBTIQ+ weddings to help readers plan a meaningful and inclusive ceremony.</li>
        <li>Conducted interviews with industry experts and celebrants to gather insights and expertise on the topic.</li>
        <li>Developed content that was sensitive to the unique needs and concerns of LGBTIQ+ couples and provided helpful advice on how to navigate potential challenges.</li>
        <li>Utilized storytelling techniques and examples from real-life ceremonies to engage readers and illustrate key points.</li>
        <li>Utilized SEO best practices to optimize the blog content for search engines and increase organic traffic to the Northfield Institute of Ceremony Guides website.</li>
      </ul>

      <h3 class="employer">Ashcombe Lodge</h3>
      <p class="position">SELF EMPLOYED / 2021-2023</p>
      <ul class="duties spaced">
        <li>Developed website content to accurately reflect Ashcombe Lodge's brand identity, mission, and offerings.</li>
        <li>Created compelling and informative copy for each section of the website, including About Us, The Venue, Free Event Guides, and Contact.</li>
      </ul>
    </div>
  </div>
</div>
</body>
</html>
```